self-employed education content specialist/consultant needs business card and logo design

I need a design for a double-sided business card (and logo) for my nascent consultancy business based in London UK, to hand out at a London trade show in a couple of weeks. The business simply has my name, "Marcus Tenwold".

I describe my service as a "content and engagement consultant". In essence I cover 2 areas:
- Advice to organisations on effective strategies and tactics for creating and distributing large volumes of media-rich content (video and interactive) for learning, training and professional development, that successfully engages and impacts on students and their teachers.
- Advice on growing and maintaining customer/end-user engagement to help maximise the reach and usage of this content.

I have uploaded a weighted list of key words that offer I hope a good feel of "the brand".

In terms of design I have put together a very rough initial idea for the card (see attached doc), which gives an idea of the key messages in text, but I feel it is not working visually, and looks too amateur. In particular I think the background/visuals of the info side needs work; the word cloud on the back of the card is perhaps rather "passé" and could be improved on; there is no "logo" at present; and I think overall it's not very "creative", i.e. it doesn't "stand out".

I am not set on font or background colours/design. The font itself should not be too businessy or too "comic sans", hence I've currently gone for something like Odile or Playfair Display.

Also note that
1. given budget and time constraints, I'm looking for designs for printing on paper, and to be of a fairly standard business card shape/size.
2. I have no web address at present, but will need a card design that can cope with this being added at a later date.

Overall I am hoping for something fairly clean, simple and clear, that will impress and speak to senior managers/business owners working in the education and edtech sectors.

As a self-employed consultant my budget is limited, so I don't expect the world for what I can offer, but am hoping that there are design experts out there who can swiftly interpret my brief and produce something suitable for my needs.

Target Market(s)

senior managers/business owners working in the education and edtech sectors.

Contact Information for Business Card

marcus tenwold
content and engagement consultant
education - training - development
+44 (0) 7731 482905
marcus.tenwold@quorvane.com

Font styles to use
Other font styles liked:
• Odile or Playfair Display are my favourites for now.

Colors

Designer to choose colors to be used in the design.

```html
<!DOCTYPE html>
<html lang="en">
<head>
<meta charset="utf-8">
<title>Marcus Tenwold – Business Card</title>
<link rel="stylesheet" href="https://fonts.googleapis.com/css2?family=Bebas+Neue&family=Montserrat:wght@400;700&display=swap">
<style>
  :root {
    --backdrop: #6d706e;
    --card-white: #ffffff;
    --brand-red: #c21d2f;
    --brand-red-light: #cb4744;
    --brand-red-mid: #c63a3b;
    --ink: #1d1d1d;
    --headline: #ffffff;
  }
  * { margin: 0; padding: 0; box-sizing: border-box; }
  html, body {
    width: 1050px;
    height: 1200px;
    overflow: hidden;
    background: var(--backdrop);
  }
  .sheet { position: relative; width: 1050px; height: 1200px; }

  .card {
    position: absolute;
    left: 140px;
    width: 770px;
    height: 437px;
    overflow: hidden;
  }

  /* Front */
  .card-front {
    top: 143px;
    background: var(--card-white);
    text-align: center;
    color: var(--ink);
    font-family: "Montserrat", sans-serif;
  }
  .brand-square {
    position: absolute;
    left: 330px;
    top: 32px;
    width: 110px;
    height: 110px;
    background: var(--brand-red);
  }
  .front-line {
    position: absolute;
    left: 0;
    width: 100%;
    transform: translateY(-50%);
    white-space: nowrap;
    font-weight: 400;
  }
  .person-name {
    top: 203px;
    font-family: "Bebas Neue", sans-serif;
    font-size: 56px;
    letter-spacing: 1px;
    color: var(--brand-red);
  }
  .role-title { top: 251px; font-size: 25px; letter-spacing: 0.5px; }
  .services { top: 287px; font-size: 25px; letter-spacing: 0.5px; }
  .services .dot { color: var(--brand-red); font-weight: 700; padding: 0 4px; }
  .divider {
    position: absolute;
    left: 330px;
    top: 321px;
    width: 110px;
    height: 3px;
    background: var(--brand-red);
  }
  .phone { top: 359px; font-size: 25px; }
  .email { top: 397px; font-size: 25px; }

  /* Back */
  .card-back {
    top: 620px;
    background: radial-gradient(ellipse at 35% 40%, var(--brand-red-light) 0%, var(--brand-red-mid) 45%, var(--brand-red) 100%);
    font-family: "Montserrat", sans-serif;
  }
  .keyword-field {
    position: absolute;
    left: 40px;
    top: 24px;
    width: 690px;
    height: 389px;
    background: radial-gradient(ellipse at 45% 45%, rgba(255, 255, 255, 0.1) 0%, rgba(255, 255, 255, 0.04) 60%, rgba(255, 255, 255, 0) 100%);
  }
  .headline {
    position: absolute;
    left: 0;
    top: 207px;
    width: 100%;
    transform: translateY(-50%);
    text-align: center;
    color: var(--headline);
    font-weight: 700;
    font-size: 100px;
    line-height: 1;
    letter-spacing: 2px;
  }
</style>
</head>
<body>
<div class="sheet">

  <section class="card card-front">
    <div class="brand-square"></div>
    <h1 class="front-line person-name">Marcus Tenwold</h1>
    <p class="front-line role-title">content and engagement consultant</p>
    <p class="front-line services">education <span class="dot">•</span> training <span class="dot">•</span> development</p>
    <div class="divider"></div>
    <p class="front-line phone">+44 (0) 7731 482905</p>
    <p class="front-line email">marcus.tenwold@quorvane.com</p>
  </section>

  <section class="card card-back">
    <div class="keyword-field" role="img" aria-label="Decorative field of pale service keywords around the headline"></div>
    <p class="headline">CONTENT</p>
  </section>

</div>
</body>
</html>
```